Kestra Health- Welcome

Under New Management / New Staff & New Physicians

Offering More Services

Accepting New Patients

Two Locations in the Bronx: North Bronx: 2915 Pellam Road – Office Phone: 718-555-0143
South Bronx: 564 Corvin Street – Office Phone: 718-555-0187

Our Services:
Primary Care
Gynecology
Cardiology
Dentistry
Psychology
Psychiatry
Neurology
Pain Management
Gastroenterology
Podiatry
Dermatology
Vascular Surgery
Physical Therapy
HIV / Infectious Disease

For an ZRPQ Mailing - we will drop off to Post Office

Front English
Back Smaller to have post office specs but have it in Spanish

```html
<!DOCTYPE html>
<html lang="en">
<head>
<meta charset="utf-8">
<title>Kestra Health – Postcard</title>
<link href="https://fonts.googleapis.com/css2?family=Montserrat:ital,wght@0,400;0,500;0,700;0,800;1,800&display=swap" rel="stylesheet">
<style>
:root{
  --blue:#22409a;
  --red:#c0202a;
  --ink:#1e1e1e;
  --white:#ffffff;
  --stage:#e6e6e8;
  --rule:#333333;
}
*{margin:0;padding:0;box-sizing:border-box}
html,body{width:932px;height:1200px;overflow:hidden;background:var(--stage);font-family:"Montserrat",sans-serif;color:var(--ink)}
.card{position:absolute;left:91px;width:751px;background:var(--white);overflow:hidden;box-shadow:0 4px 10px rgba(0,0,0,.25)}
.card--front{top:66px;height:511px}
.card--back{top:625px;height:509px}
.abs{position:absolute}
.panel{position:absolute;left:0;top:0}
.brand{position:absolute;display:flex;align-items:center;gap:8px;font-weight:800;color:var(--blue);white-space:nowrap}
.brand__mark{background:var(--red);display:block}
.badge{position:absolute;display:flex;align-items:center}
.badge__icon{flex:none}
.badge__text{color:var(--white);font-weight:800;font-style:italic;line-height:1.1}
.heading{position:absolute;color:var(--blue);font-weight:700;white-space:nowrap}
.services{position:absolute;list-style:none}
.services li{position:relative;white-space:nowrap}
.services li::before{content:"+";position:absolute;color:var(--red);font-weight:700}
.front-services li{font-size:15.5px;height:23.3px;line-height:23.3px;padding-left:20px}
.front-services li::before{left:2px;font-size:14px}
.back-services li{font-size:11px;height:18.1px;line-height:18.1px;padding-left:13px}
.back-services li::before{left:0;font-size:10px}
.loc{position:absolute;white-space:nowrap;display:flex;align-items:center;gap:6px}
.front-loc{font-size:15.5px}
.back-loc{font-size:11px;color:var(--white)}
.photo{position:absolute;left:393px;top:318px;width:358px;height:193px;background:linear-gradient(90deg,rgba(255,255,255,0) 0%,#c9b2a0 18%,#7d9fd6 45%,#6f5447 70%,#e9d7de 100%)}
.stamp{position:absolute;left:605px;top:47px;width:95px;height:118px;border:1px solid var(--rule)}
.address-line{position:absolute;left:398px;width:302px;height:1px;background:var(--rule)}
.divider{position:absolute;left:163px;top:437px;width:1.5px;height:42px;background:var(--red)}
</style>
</head>
<body>
<svg width="0" height="0" style="position:absolute">
  <defs>
    <symbol id="pin" viewBox="0 0 12 16"><path d="M6 0C2.7 0 0 2.6 0 5.9 0 10.3 6 16 6 16s6-5.7 6-10.1C12 2.6 9.3 0 6 0zm0 8.3a2.4 2.4 0 1 1 0-4.8 2.4 2.4 0 0 1 0 4.8z"/></symbol>
    <symbol id="phone" viewBox="0 0 16 16"><path d="M3.6 0.6l2.3 2.9c.3.4.3 1-.1 1.4L4.5 6.2c.9 2.1 3.2 4.4 5.3 5.3l1.3-1.3c.4-.4 1-.4 1.4-.1l2.9 2.3c.4.3.5 1 .1 1.4l-1.4 1.5c-.6.6-1.5.8-2.3.5C6.8 14.2 1.8 9.2.2 4.2-.1 3.4.1 2.5.7 1.9L2.2.5c.4-.4 1.1-.3 1.4.1z"/></symbol>
    <symbol id="cross-badge" viewBox="0 0 44 40"><path d="M6 0H44L38 40H0Z" fill="#c0202a"/><path d="M18.5 10h6v7h7v6h-7v7h-6v-7h-7v-6h7z" fill="#fff"/></symbol>
  </defs>
</svg>

<!-- Front: English -->
<section class="card card--front">
  <svg class="panel" width="751" height="511" viewBox="0 0 751 511" aria-hidden="true">
    <path d="M357 0H751V179H330Q296 179 306 150L357 0Z" fill="#22409a"/>
  </svg>

  <div class="brand" style="left:50px;top:84px;font-size:32px">
    <span class="brand__mark" style="width:14px;height:14px"></span>Kestra Health
  </div>

  <div class="badge" style="left:368px;top:48px">
    <svg class="badge__icon" width="44" height="40"><use href="#cross-badge"/></svg>
    <span class="badge__text" style="margin-left:12px;font-size:19px">Under New Management /<br>New Staff &amp; New Physicians</span>
  </div>
  <div class="badge" style="left:334px;top:116px">
    <svg class="badge__icon" width="44" height="40"><use href="#cross-badge"/></svg>
    <span class="badge__text" style="margin-left:11px;font-size:19px">Offering More<br>Services</span>
  </div>
  <div class="badge" style="left:538px;top:116px">
    <svg class="badge__icon" width="44" height="40"><use href="#cross-badge"/></svg>
    <span class="badge__text" style="margin-left:11px;font-size:19px">Accepting<br>New Patients</span>
  </div>

  <h2 class="heading" style="left:51px;top:163px;font-size:22px">Our Services:</h2>
  <ul class="services front-services" style="left:53px;top:208px">
    <li>Primary Care</li><li>Gynecology</li><li>Cardiology</li><li>Dentistry</li><li>Psychology</li>
  </ul>
  <ul class="services front-services" style="left:233px;top:208px">
    <li>Psychiatry</li><li>Neurology</li><li>Pain Management</li><li>Gastroenterology</li><li>Podiatry</li>
  </ul>
  <ul class="services front-services" style="left:436px;top:208px">
    <li>Dermatology</li><li>Vascular Surgery</li><li>Physical Therapy</li><li>HIV / Infectious Disease</li>
  </ul>

  <h2 class="heading" style="left:51px;top:343px;font-size:22px">Two Locations in the Bronx</h2>
  <div class="loc front-loc" style="left:53px;top:378px">North Bronx</div>
  <div class="loc front-loc" style="left:53px;top:399px">
    <svg width="11" height="14" fill="#c0202a"><use href="#pin"/></svg>2915 Pellam Road&nbsp;&nbsp;|&nbsp;
    <svg width="13" height="13" fill="#c0202a"><use href="#phone"/></svg>718-555-0143
  </div>
  <div class="loc front-loc" style="left:53px;top:432px">South Bronx</div>
  <div class="loc front-loc" style="left:53px;top:453px">
    <svg width="11" height="14" fill="#c0202a"><use href="#pin"/></svg>564 Corvin Street&nbsp;&nbsp;|&nbsp;
    <svg width="13" height="13" fill="#c0202a"><use href="#phone"/></svg>718-555-0187
  </div>

  <div class="photo" role="img" aria-label="Photo of a smiling team of doctors and nurses in white coats and blue scrubs"></div>
</section>

<!-- Back: Spanish, mailing side -->
<section class="card card--back">
  <svg class="panel" width="751" height="509" viewBox="0 0 751 509" aria-hidden="true">
    <path d="M264 0H375V235H0V121H218Q244 121 254 98L264 0Z" fill="#22409a"/>
    <path d="M264 0L218 98" stroke="none"/>
    <path d="M0 401H355Q375 401 375 381V509H0Z" fill="#22409a"/>
  </svg>

  <div class="brand" style="left:38px;top:58px;font-size:22px;gap:6px">
    <span class="brand__mark" style="width:10px;height:10px"></span>Kestra Health
  </div>

  <div class="badge" style="left:34px;top:141px">
    <svg class="badge__icon" width="33" height="30"><use href="#cross-badge"/></svg>
    <span class="badge__text" style="margin-left:9px;font-size:13.5px">Bajo nueva dirección /<br>nuevo personal y nuevos médicos</span>
  </div>
  <div class="badge" style="left:34px;top:188px">
    <svg class="badge__icon" width="33" height="30"><use href="#cross-badge"/></svg>
    <span class="badge__text" style="margin-left:9px;font-size:13.5px">Ofreciendo<br>más servicios</span>
  </div>
  <div class="badge" style="left:188px;top:188px">
    <svg class="badge__icon" width="33" height="30"><use href="#cross-badge"/></svg>
    <span class="badge__text" style="margin-left:9px;font-size:13.5px">Aceptando<br>pacientes nuevos</span>
  </div>

  <h2 class="heading" style="left:34px;top:246px;font-size:16px">Nuestros servicios:</h2>
  <ul class="services back-services" style="left:35px;top:271px">
    <li>Atención primaria</li><li>Ginecología</li><li>Cardiología</li><li>Odontología</li><li>Psicología</li><li>Psiquiatría</li><li>Neurología</li>
  </ul>
  <ul class="services back-services" style="left:174px;top:271px">
    <li>El manejo del dolor</li><li>Gastroenterología</li><li>Podología</li><li>Dermatología</li><li>Cirugía vascular</li><li>Terapia física</li><li>VIH / Enfermedad Infecciosa</li>
  </ul>

  <h2 class="heading" style="left:36px;top:410px;font-size:15.5px;color:var(--white)">Dos ubicaciones en el Bronx:</h2>
  <div class="loc back-loc" style="left:36px;top:434px">North Bronx</div>
  <div class="loc back-loc" style="left:36px;top:450px;gap:4px"><svg width="8" height="10" fill="#fff"><use href="#pin"/></svg>2915 Pellam Road</div>
  <div class="loc back-loc" style="left:36px;top:466px;gap:4px"><svg width="9" height="9" fill="#fff"><use href="#phone"/></svg>718-555-0143</div>
  <div class="divider"></div>
  <div class="loc back-loc" style="left:194px;top:434px">South Bronx</div>
  <div class="loc back-loc" style="left:194px;top:450px;gap:4px"><svg width="8" height="10" fill="#fff"><use href="#pin"/></svg>564 Corvin Street</div>
  <div class="loc back-loc" style="left:194px;top:465px;gap:4px"><svg width="9" height="9" fill="#fff"><use href="#phone"/></svg>718-555-0187</div>

  <div class="stamp"></div>
  <div class="address-line" style="top:283px"></div>
  <div class="address-line" style="top:336px"></div>
  <div class="address-line" style="top:389px"></div>
  <div class="address-line" style="top:442px"></div>
</section>
</body>
</html>
```